VENTURE CAPITAL GROUP BUSINESS CARD DESIGN

Venture Capital Group based in SF looking for a bold business card design. No trendy colour explosion, 3D effects etc. Just "simple" optical effects. Works on your brain, keeps your eye focused and sticks to your mind.
Target Market(s)
Technology startups
Industry/Entity Type
Venture Capital
Contact Information for Business Card
BARNABY WHITLOCK
MANAGING PARTNER
817 FERN ST SAN FRANCISCO, CA 94111
415.555.0143 O
415.555.0167 F
415.555.0192 C
barn@halcyonridgefund.example

```html
<!DOCTYPE html>
<html lang="en">
<head>
<meta charset="utf-8">
<title>Halcyon Ridge – Business Card</title>
<link rel="stylesheet" href="https://fonts.googleapis.com/css2?family=Marcellus&family=Quattrocento:wght@400;700&display=swap">
<style>
  :root {
    --backdrop: #a9a7a8;
    --card: #1a1b1d;
    --green: #2f9a3e;
    --green-light: #5cbf55;
    --green-dark: #136a32;
    --silver: #c9c9c9;
    --text: #d9d9d9;
    --muted: #b5b5b5;
    --tagline: #8e8e8e;
    --icon: #2f9a3e;
    --disc: #2a2a2c;
  }
  * { margin: 0; padding: 0; box-sizing: border-box; }
  html, body { width: 1200px; height: 1200px; overflow: hidden; }
  body { background: var(--backdrop); position: relative; font-family: "Quattrocento", serif; }

  .card { position: absolute; background: var(--card); overflow: hidden; }
  .card-front { left: 237px; top: 116px; width: 715px; height: 422px; }
  .card-back  { left: 229px; top: 644px; width: 715px; height: 418px; }

  .brand-disc { border-radius: 50%; background: var(--disc); flex: none; display: block; }
  .brand-text { display: flex; flex-direction: column; align-items: center; }
  .brand-name {
    font-family: "Marcellus", serif; color: var(--green);
    text-transform: uppercase; letter-spacing: 0.02em; white-space: nowrap; line-height: 1;
  }
  .brand-tagline {
    font-family: "Marcellus", serif; color: var(--tagline);
    text-transform: uppercase; white-space: nowrap; line-height: 1;
  }

  /* front: stacked, centred */
  .card-front .brand-disc { position: absolute; left: 271px; top: 87px; width: 172px; height: 172px; }
  .card-front .brand-text { position: absolute; left: 0; right: 0; top: 280px; }
  .card-front .brand-name { font-size: 48px; }
  .card-front .brand-tagline { font-size: 14px; letter-spacing: 0.42em; margin-top: 6px; padding-left: 0.42em; }

  .side-band {
    position: absolute; left: 0; top: 0; bottom: 0; width: 60px;
    background: linear-gradient(180deg, var(--green-light), var(--green) 45%, var(--green-dark));
  }
  .side-rule { position: absolute; left: 60px; top: 0; bottom: 0; width: 7px; background: var(--silver); }

  /* back: disc beside stacked wordmark */
  .card-back .brand-disc { position: absolute; left: 94px; top: 46px; width: 96px; height: 96px; }
  .card-back .brand-text { position: absolute; left: 217px; top: 66px; }
  .card-back .brand-name { font-size: 40px; }
  .card-back .brand-tagline { font-size: 12px; letter-spacing: 0.42em; margin-top: 6px; padding-left: 0.42em; }

  .person { position: absolute; left: 93px; top: 210px; }
  .person-name { font-size: 25px; font-weight: 700; color: var(--text); }
  .person-title { font-size: 16px; color: var(--muted); margin-top: 3px; }

  .contact-list { position: absolute; top: 303px; list-style: none; }
  .contact-list li { display: flex; align-items: center; height: 26px; font-size: 17px; color: var(--text); }
  .contact-list svg { width: 16px; height: 16px; margin-right: 12px; fill: var(--icon); flex: none; }
  .contact-phones { left: 93px; }
  .contact-details { left: 315px; }
</style>
</head>
<body>
  <section class="card card-front">
    <span class="brand-disc"></span>
    <div class="brand-text">
      <span class="brand-name">Halcyon Ridge</span>
      <span class="brand-tagline">Capital Group</span>
    </div>
  </section>

  <section class="card card-back">
    <div class="side-band"></div>
    <div class="side-rule"></div>

    <span class="brand-disc"></span>
    <div class="brand-text">
      <span class="brand-name">Halcyon Ridge</span>
      <span class="brand-tagline">Capital Group</span>
    </div>

    <div class="person">
      <p class="person-name">Barnaby Whitlock</p>
      <p class="person-title">Managing Partner</p>
    </div>

    <ul class="contact-list contact-phones">
      <li><svg viewBox="0 0 16 16" aria-hidden="true"><path d="M2 6c0-2 2-3 6-3s6 1 6 3v1h-3V6H5v1H2z"/><rect x="3" y="8" width="10" height="6" rx="1"/></svg>415.555.0143</li>
      <li><svg viewBox="0 0 16 16" aria-hidden="true"><rect x="4" y="1" width="8" height="4"/><rect x="1" y="6" width="14" height="6" rx="1"/><rect x="4" y="10" width="8" height="5"/></svg>415.555.0167</li>
      <li><svg viewBox="0 0 16 16" aria-hidden="true"><path d="M4 1h8v14H4zM5.5 3v9h5V3z"/></svg>415.555.0192</li>
    </ul>

    <ul class="contact-list contact-details">
      <li><svg viewBox="0 0 16 16" aria-hidden="true"><path d="M1 3h14v10H1zM2 4.2v.6l6 4 6-4v-.6z"/></svg>Barn@halcyonridgefund.example</li>
      <li><svg viewBox="0 0 16 16" aria-hidden="true"><path d="M8 1a7 7 0 1 0 0 14A7 7 0 0 0 8 1zm-1 2v4H3.1A5 5 0 0 1 7 3zm2 0a5 5 0 0 1 3.9 4H9zM3.1 9H7v4A5 5 0 0 1 3.1 9zM9 9h3.9A5 5 0 0 1 9 13z"/></svg>www.halcyonridgefund.example</li>
      <li><svg viewBox="0 0 16 16" aria-hidden="true"><path d="M8 1a5 5 0 0 0-5 5c0 4 5 9 5 9s5-5 5-9a5 5 0 0 0-5-5zm0 3a2 2 0 1 1 0 4 2 2 0 0 1 0-4z"/></svg>817 Fern St San Francisco, CA 94111</li>
    </ul>
  </section>
</body>
</html>
```